Business Card Design for retail pharmacist based in Sydney, Australia

I need a professional, health care oriented business card for a reatil pharmacist providing health advice and information

```html
<!DOCTYPE html>
<html lang="en">
<head>
<meta charset="utf-8">
<title>Daniel Marsh – Business Card</title>
<link rel="stylesheet" href="https://fonts.googleapis.com/css2?family=Patrick+Hand&family=Arimo:wght@400&family=PT+Sans:wght@400&display=swap">
<style>
  :root {
    --page-bg: #e9e6e1;
    --red: #d8222d;
    --red-dark: #b81b26;
    --red-light: #e5353f;
    --band: #5a7184;
    --navy: #1f3a56;
    --navy-dark: #183049;
    --navy-light: #2a4866;
    --white: #ffffff;
    --text-light: #e6edf3;
  }
  * { margin: 0; padding: 0; box-sizing: border-box; }
  html, body {
    width: 1200px;
    height: 800px;
    overflow: hidden;
    background: var(--page-bg);
  }
  .sheet {
    position: relative;
    width: 1200px;
    height: 800px;
    display: flex;
    align-items: center;
    justify-content: center;
    gap: 40px;
  }
  .card {
    position: relative;
    width: 540px;
    height: 324px;
    overflow: hidden;
    box-shadow: 0 6px 16px rgba(0,0,0,0.28);
  }
  .card-art {
    position: absolute;
    inset: 0;
    width: 100%;
    height: 100%;
  }
  .card-front .holder {
    position: absolute;
    left: 32px;
    top: 236px;
    color: var(--white);
  }
  .holder-name {
    font-family: "Patrick Hand", cursive;
    font-weight: 400;
    font-size: 34px;
    line-height: 1;
    letter-spacing: 1px;
  }
  .holder-role {
    font-family: "Arimo", Arial, sans-serif;
    font-size: 14px;
    margin-top: 8px;
  }
  .card-back .motif {
    position: absolute;
    left: 20px;
    top: 0;
    width: 240px;
    height: 270px;
    background: radial-gradient(ellipse at 45% 40%, rgba(110,150,185,0.35), rgba(110,150,185,0) 70%);
  }
  .details {
    position: absolute;
    left: 200px;
    top: 144px;
    font-family: "PT Sans", Arial, sans-serif;
    font-size: 16px;
    color: var(--text-light);
    list-style: none;
  }
  .details li {
    display: flex;
    height: 25px;
    align-items: center;
    white-space: nowrap;
  }
  .details .label {
    width: 36px;
  }
  .details .credentials {
    padding-left: 36px;
  }
</style>
</head>
<body>
<main class="sheet">

  <section class="card card-front">
    <svg class="card-art" viewBox="0 0 540 324" aria-hidden="true">
      <rect x="0" y="0" width="410" height="324" fill="var(--red)"/>
      <polygon points="0,0 240,0 110,190 0,150" fill="var(--red-dark)" opacity="0.55"/>
      <polygon points="110,0 410,0 410,140 230,230" fill="var(--red-light)" opacity="0.45"/>
      <polygon points="0,150 110,190 55,324 0,324" fill="var(--red-dark)" opacity="0.35"/>
      <polygon points="230,230 410,140 410,324 190,324" fill="var(--red-dark)" opacity="0.3"/>
      <polygon points="300,0 410,0 410,90" fill="var(--red-dark)" opacity="0.4"/>
      <rect x="410" y="0" width="40" height="324" fill="var(--band)"/>
      <rect x="450" y="0" width="90" height="324" fill="var(--navy)"/>
      <polygon points="450,0 540,0 540,140" fill="var(--navy-light)" opacity="0.7"/>
      <polygon points="450,210 540,170 540,324 450,324" fill="var(--navy-dark)" opacity="0.7"/>
      <rect class="accent-square" x="386" y="116" width="88" height="88" fill="var(--white)"/>
    </svg>
    <div class="holder">
      <h1 class="holder-name">Daniel Marsh</h1>
      <p class="holder-role">Health Care Professional</p>
    </div>
  </section>

  <section class="card card-back">
    <svg class="card-art" viewBox="0 0 540 324" aria-hidden="true">
      <rect width="540" height="324" fill="var(--navy)"/>
      <polygon points="0,0 300,0 120,324 0,324" fill="var(--navy-dark)" opacity="0.45"/>
      <polygon points="300,0 540,0 540,180 380,130" fill="var(--navy-light)" opacity="0.55"/>
      <polygon points="380,130 540,180 540,324 260,324" fill="var(--navy-dark)" opacity="0.35"/>
    </svg>
    <div class="motif" role="img" aria-label="Faint sketched emblem decoration"></div>
    <ul class="details">
      <li class="credentials">B. Pharm (Hons I, Uni Medal), MPS</li>
      <li><span class="label">e.</span>info@harbourchemist.com.au</li>
      <li><span class="label">m.</span>0400 555 018</li>
      <li><span class="label">a.</span>Seaview Pharmacy: 02 9000 1234</li>
      <li><span class="label">a.</span>Ridgeway Pharmacy: 02 9000 5678</li>
    </ul>
  </section>

</main>
</body>
</html>
```